Groovy little Insurance brokerage needs a new look

We have a new logo, but need to work out how to make it work for us!
We are a small insurance broking firm (three staff with different focus and styles), with lots of energy, experience and enthusiasm. A focus on both commercial and domestic market. We would like our cards to show a fresh look - while veering away from the 'run of the mill' insurance industry (often dull) approach.
Updates

Thanks to all for your concepts.

Had some great ideas come back, now just the process of picking which one is going to work best for us...
Will advise when we've had an opportunity to review.

Thanks!
From the team at
Kestrel Dunmore Insurance Brokers

Thanks SO much to all of your for your great designs.  Now just a process of sorting out the favorites.  If yours is eliminated, just want to say a collective thank you for your efforts!

Industry/Entity Type

Business

```html
<!DOCTYPE html>
<html lang="en">
<head>
<meta charset="utf-8">
<title>Kestrel Dunmore Insurance Brokers – Business Card</title>
<link rel="stylesheet" href="https://fonts.googleapis.com/css2?family=Quicksand:wght@400;500;600;700&display=swap">
<style>
  :root {
    --teal: #3bb3c8;
    --teal-soft: #8fd3df;
    --ink: #3a3a3c;
    --grey: #6e6e70;
    --grey-light: #9a9a9c;
    --card: #ffffff;
    --backdrop: #e9e7e3;
  }
  * { box-sizing: border-box; margin: 0; padding: 0; }
  html, body {
    width: 1200px;
    height: 1184px;
    overflow: hidden;
    background: var(--backdrop);
    font-family: "Quicksand", sans-serif;
  }
  .business-card {
    position: absolute;
    left: 100px;
    top: 312px;
    width: 1000px;
    height: 560px;
    background: linear-gradient(100deg, var(--card) 55%, #f3f3f3 100%);
    box-shadow: 0 18px 40px rgba(0,0,0,0.18);
  }
  .brand {
    position: absolute;
    left: 80px;
    top: 218px;
    display: flex;
    align-items: center;
    gap: 22px;
  }
  .brand-square {
    width: 112px;
    height: 112px;
    background: var(--teal);
    flex: none;
  }
  .brand-name {
    width: 290px;
    font-size: 28px;
    line-height: 1.2;
    font-weight: 700;
    color: var(--ink);
  }
  .divider {
    position: absolute;
    left: 560px;
    top: 110px;
    width: 2px;
    height: 340px;
    background: var(--teal);
  }
  .contact {
    position: absolute;
    left: 590px;
    top: 104px;
  }
  .person-name {
    font-size: 34px;
    letter-spacing: 0.5px;
    color: var(--teal);
    font-weight: 400;
  }
  .person-name strong { font-weight: 600; }
  .person-title {
    margin-top: 2px;
    font-size: 15px;
    letter-spacing: 9px;
    color: var(--grey-light);
  }
  .contact-list {
    list-style: none;
    margin-top: 64px;
  }
  .contact-list li {
    display: flex;
    align-items: flex-start;
    gap: 16px;
    font-size: 18px;
    letter-spacing: 1.2px;
    color: var(--grey);
    margin-bottom: 14px;
  }
  .contact-list li.address { margin-top: 24px; line-height: 1.45; }
  .contact-list svg { width: 18px; height: 18px; flex: none; margin-top: 3px; fill: var(--teal); }
</style>
</head>
<body>
  <article class="business-card">
    <div class="brand">
      <div class="brand-square"></div>
      <div class="brand-name">Kestrel Dunmore Insurance Brokers</div>
    </div>

    <div class="divider"></div>

    <section class="contact">
      <h1 class="person-name"><strong>NAME</strong>SURNAME</h1>
      <p class="person-title">TITLE</p>
      <ul class="contact-list">
        <li class="phone">
          <svg viewBox="0 0 18 18" aria-hidden="true"><rect x="4" y="1" width="10" height="16" rx="2"/><rect x="6" y="3.5" width="6" height="8" fill="#fff"/><circle cx="9" cy="14" r="1.2" fill="#fff"/></svg>
          <span>555.014.2290</span>
        </li>
        <li class="email">
          <svg viewBox="0 0 18 18" aria-hidden="true"><rect x="1" y="4" width="16" height="11" rx="1"/><path d="M1.5 4.5 L9 10.5 L16.5 4.5" stroke="#fff" stroke-width="1.4" fill="none"/></svg>
          <span>ava@kestreldunmore.com</span>
        </li>
        <li class="address">
          <svg viewBox="0 0 18 18" aria-hidden="true"><path d="M9 1a5.5 5.5 0 0 0-5.5 5.5C3.5 11 9 17 9 17s5.5-6 5.5-10.5A5.5 5.5 0 0 0 9 1z"/><circle cx="9" cy="6.5" r="2" fill="#fff"/></svg>
          <span>4210 HARBOUR LANE,<br>STE 300, FAIRVIEW, FL 33000</span>
        </li>
      </ul>
    </section>
  </article>
</body>
</html>
```